General Contractors need a new Crisp updated Card Design

We need a new business card design for our company of 25 years based in Toronto call Holvaster Building Inc. : Our goal is to be the leading commercial contractors in Toronto by providing exceptional value to our clients. We work very hard to deliver professional, quality, service in conjunction with consistent price competitiveness to all of our clients on every single project.

Target Market(s)

Design & Build Clients

Industry/Entity Type

Construction Company

Contact Information for Business Card

Address:
18 North Tamlin Glen Road, Unit 57, Marbrook Vale, ON, K7T 2R9
Office: 905-218-5937

Holvasters Logo
Employee Job Description
Employee Cell Phone #
Employee Email
www.holvaster-example.com

Colors

Designer to choose colors to be used in the design.

Requirements
Must have
• Quote Company Saying:
• "Professional. Quality. Service."
Nice to have
• New Crisp up to date look. simple & fresh ( Not to Busy)
Should not have
• NO BLUE PRINTS ON THE BUSINESS CARDS

```html
<!DOCTYPE html>
<html lang="en">
<head>
<meta charset="utf-8">
<title>Holvaster Building Inc. – Business Card</title>
<link rel="stylesheet" href="https://fonts.googleapis.com/css2?family=Lato:wght@400;700&family=Montserrat:wght@700&display=swap">
<style>
  :root {
    --teal: #0f9188;
    --teal-deep: #0a7c74;
    --paper: #f4f4f2;
    --ground: #2b2b2b;
    --ink-light: #ffffff;
  }
  * { box-sizing: border-box; margin: 0; padding: 0; }
  html, body { width: 1200px; height: 900px; overflow: hidden; }
  body {
    background: var(--ground);
    font-family: "Lato", sans-serif;
    position: relative;
  }
  .card {
    position: absolute;
    left: 250px;
    width: 700px;
    height: 400px;
    background: var(--paper);
    overflow: hidden;
    box-shadow: 0 10px 30px rgba(0,0,0,.45);
  }
  .card--front { top: 40px; }
  .card--back { top: 470px; }

  /* Front */
  .front__band {
    position: absolute; left: 70px; top: 0;
    width: 140px; height: 100%;
    background: linear-gradient(160deg, var(--teal), var(--teal-deep));
  }
  .front__motto {
    position: absolute; left: 140px; top: 200px;
    transform: translate(-50%, -50%) rotate(-90deg);
    white-space: nowrap;
    color: var(--ink-light);
    font-size: 15px; letter-spacing: 3px;
  }
  .front__bar-top {
    position: absolute; right: 0; top: 0;
    width: 320px; height: 24px; background: var(--teal);
  }
  .front__bar-bottom {
    position: absolute; right: 0; bottom: 0;
    width: 150px; height: 30px; background: var(--teal);
  }
  .brand {
    position: absolute; display: flex; align-items: center; gap: 14px;
    white-space: nowrap;
  }
  .brand__mark { width: 46px; height: 46px; }
  .brand__name { font-weight: 700; }
  .front__brand { left: 280px; top: 172px; color: var(--teal); }
  .front__brand .brand__name { font-size: 34px; }
  .front__brand .brand__mark { background: var(--teal); }

  /* Back */
  .back__band-top {
    position: absolute; left: 0; top: 0; width: 100%; height: 115px;
    background: linear-gradient(160deg, var(--teal), var(--teal-deep));
  }
  .back__brand { left: 190px; top: 38px; color: var(--ink-light); }
  .back__brand .brand__name { font-size: 26px; }
  .back__brand .brand__mark { width: 36px; height: 36px; background: var(--ink-light); }
  .person {
    position: absolute; left: 60px; top: 175px; text-align: right; width: 270px;
    color: var(--teal);
  }
  .person__name {
    font-family: "Montserrat", sans-serif; font-weight: 700; font-size: 32px;
  }
  .person__title { font-size: 18px; margin-top: 2px; }
  .divider {
    position: absolute; left: 370px; top: 140px; width: 1px; height: 150px;
    background: var(--teal);
  }
  .contacts {
    position: absolute; left: 400px; top: 148px; list-style: none;
    color: var(--teal); font-size: 16px;
  }
  .contacts li { display: flex; align-items: center; gap: 12px; height: 33px; }
  .contacts svg { width: 15px; height: 15px; fill: var(--teal); flex: none; }
  .back__band-bottom {
    position: absolute; left: 0; bottom: 0; width: 100%; height: 88px;
    background: linear-gradient(160deg, var(--teal), var(--teal-deep));
    display: flex; align-items: center; justify-content: center; gap: 10px;
    color: var(--ink-light); font-size: 17px;
  }
  .back__band-bottom svg { width: 14px; height: 18px; fill: var(--ink-light); }
</style>
</head>
<body>
  <section class="card card--front">
    <div class="front__band"></div>
    <p class="front__motto">PROFESSIONAL. QUALITY. SERVICE</p>
    <div class="front__bar-top"></div>
    <div class="front__bar-bottom"></div>
    <div class="brand front__brand">
      <span class="brand__mark"></span>
      <span class="brand__name">Holvaster Building Inc.</span>
    </div>
  </section>

  <section class="card card--back">
    <div class="back__band-top"></div>
    <div class="brand back__brand">
      <span class="brand__mark"></span>
      <span class="brand__name">Holvaster Building Inc.</span>
    </div>

    <div class="person">
      <p class="person__name">YOUR NAME</p>
      <p class="person__title">Job Title</p>
    </div>
    <div class="divider"></div>
    <ul class="contacts">
      <li><svg viewBox="0 0 24 24"><path d="M6.6 10.8a15.1 15.1 0 0 0 6.6 6.6l2.2-2.2a1 1 0 0 1 1-.25 11.4 11.4 0 0 0 3.6.57 1 1 0 0 1 1 1V20a1 1 0 0 1-1 1A17 17 0 0 1 3 4a1 1 0 0 1 1-1h3.5a1 1 0 0 1 1 1c0 1.25.2 2.45.57 3.57a1 1 0 0 1-.25 1z"/></svg>905-218-5937</li>
      <li><svg viewBox="0 0 24 24"><path d="M7 1h10a2 2 0 0 1 2 2v18a2 2 0 0 1-2 2H7a2 2 0 0 1-2-2V3a2 2 0 0 1 2-2zm0 3v14h10V4zm5 15.5a1 1 0 1 0 0 2 1 1 0 0 0 0-2z"/></svg>000 000 0000</li>
      <li><svg viewBox="0 0 24 24"><path d="M12 2a10 10 0 1 0 0 20 10 10 0 0 0 0-20zm6.9 6h-3a15.6 15.6 0 0 0-1.4-3.6A8 8 0 0 1 18.9 8zM12 4c.8 1.2 1.5 2.5 1.9 4h-3.8c.4-1.5 1.1-2.8 1.9-4zM4.3 14a8 8 0 0 1 0-4h3.4a16.5 16.5 0 0 0 0 4zm.8 2h3a15.6 15.6 0 0 0 1.4 3.6A8 8 0 0 1 5.1 16zm3-8h-3a8 8 0 0 1 4.3-3.6A15.6 15.6 0 0 0 8.1 8zM12 20c-.8-1.2-1.5-2.5-1.9-4h3.8c-.4 1.5-1.1 2.8-1.9 4zm2.3-6H9.7a14.7 14.7 0 0 1 0-4h4.6a14.7 14.7 0 0 1 0 4zm.3 5.6a15.6 15.6 0 0 0 1.4-3.6h3a8 8 0 0 1-4.4 3.6zm1.7-5.6a16.5 16.5 0 0 0 0-4h3.4a8 8 0 0 1 0 4z"/></svg>www.holvaster-example.com</li>
      <li><svg viewBox="0 0 24 24"><path d="M2 5h20v14H2zm2 2v.5l8 5 8-5V7zm0 2.8V17h16V9.8l-8 5z"/></svg>youremail@holvaster-example.com</li>
    </ul>

    <div class="back__band-bottom">
      <svg viewBox="0 0 24 30"><path d="M12 0a10 10 0 0 0-10 10c0 7.5 10 20 10 20s10-12.5 10-20A10 10 0 0 0 12 0zm0 14a4 4 0 1 1 0-8 4 4 0 0 1 0 8z"/></svg>
      <span>18 North Tamlin Glen Road, Unit 57, Marbrook Vale, ON, K7T 2R9</span>
    </div>
  </section>
</body>
</html>
```